Fresh, modern brand required for new start-up!

TallCropNear is a new venture offering an end-to-end communications and media relations service including strategy development, execution and evaluation; copy writing and editing; social and e- media management; leadership coaching, media training and more.

I require a fresh and lively corporate identity to mirror the ethos of the business.

I need a logo, business card (double-sided preferably), letterhead (for invoicing and client communications) and compliment slip. As a start-up, budget will be an ongoing consideration for me so, ideally, I would prefer a two-colour logo - although if you wow me with something more than that, I may have to throw caution to the wind!

The ethos behind my name is twofold; one, I have moved from being something of a "big fish in a small pond" (a director in a single company) to a small fish in the big pond of small businesses. Two, I may be a "small fish", but that doesn't mean I don't "fish big".

I am looking for a clean, simple design that will look good on a variety of mediums, big or small. The design should be young and fresh and make an immediate impact. I want the design to reflect the fact that I specialise in tailored, simple and effective communications.

Target Market(s)

My clients range from global financial services, resources and technology companies to not-for-profit organisations and other small businesses. Moreover, my current client base stretches from Asia Pacific (incl. Australia), to Europe (incl. UK) and the US. All my clients speak English (even if as a second language) and are relatively senior communications professionals within their organisations.

Industry/Entity Type

Communications

Requirements
Nice to have
• The design/logo could include symbols and/or characters that double as imagery. For example: an upside down question mark (?) might look like a fishing line/hook and a flattened @ sign, might look like a pond...
Should not have
• The design should not use old-style serif fonts, but nor should it be "cartoony" in any way. No navy blue, grey or sombre corporate colours.

```html
<!DOCTYPE html>
<html lang="en">
<head>
<meta charset="utf-8">
<title>TallCropNear stationery</title>
<link rel="stylesheet" href="https://fonts.googleapis.com/css2?family=Open+Sans:wght@400;600&display=swap">
<style>
  :root {
    --ink: #111111;
    --sky: #6cc8e2;
    --orange: #f08a2e;
    --paper: #ffffff;
    --backdrop: #ffffff;
    --aqua-pale: #9fd6d6;
    --orange-deep: #e8731c;
  }
  * { box-sizing: border-box; margin: 0; padding: 0; }
  html, body { width: 1200px; height: 900px; overflow: hidden; background: var(--backdrop); }
  body { position: relative; font-family: "Open Sans", Arial, sans-serif; color: var(--ink); }

  .sheet {
    position: absolute; background: var(--paper);
    box-shadow: 2px 3px 6px rgba(0,0,0,0.45);
  }
  .letterhead { left: 14px; top: 18px; width: 614px; height: 870px; }
  .compliments { left: 545px; top: 385px; width: 614px; height: 290px; z-index: 2; }

  .rule { position: absolute; left: 0; right: 3px; height: 5px; background: var(--ink); }

  .contact-row {
    position: absolute; left: 6px; right: 6px; display: flex;
    font-size: 12.5px; white-space: nowrap;
  }
  .contact-row .phone { width: 142px; }
  .contact-row .street, .contact-row .town, .contact-row .country { color: var(--sky); }
  .contact-row .street { width: 119px; }
  .contact-row .town { width: 147px; }
  .contact-row .country { width: 96px; }
  .contact-row .email { margin-left: auto; }

  .salutation { position: absolute; left: 6px; top: 58px; font-size: 16px; color: var(--sky); }
  .letter-body {
    position: absolute; left: 58px; top: 100px; width: 430px;
    font-size: 10px; line-height: 13.45px; letter-spacing: 0.35px;
  }
  .letter-body p + p { margin-top: 13.45px; }
  .sign-off { position: absolute; left: 395px; top: 656px; font-size: 16px; color: var(--sky); }
  .signature-area {
    position: absolute; left: 395px; top: 682px; width: 170px; height: 58px;
    background: linear-gradient(90deg, rgba(17,17,17,0.08), rgba(17,17,17,0.02));
  }

  .brand-name { font-weight: 400; color: var(--ink); letter-spacing: -0.3px; white-space: nowrap; }
  .brand-dot { display: inline-block; border-radius: 50%; vertical-align: middle; }

  .letterhead .brand { position: absolute; left: 20px; top: 806px; display: flex; align-items: center; gap: 26px; }
  .letterhead .brand-name { font-size: 40px; }
  .letterhead .brand-dot { width: 48px; height: 48px; background: var(--sky); }

  .compliments .title { position: absolute; left: 6px; top: 52px; font-size: 21px; color: var(--orange); letter-spacing: 0.3px; }
  .compliments .brand { position: absolute; left: 2px; top: 250px; display: flex; align-items: center; gap: 14px; }
  .compliments .brand-name { font-size: 22px; }
  .compliments .brand-dot { width: 22px; height: 22px; background: var(--orange); }

  .logo-variant { position: absolute; top: 62px; display: flex; flex-direction: column; align-items: center; gap: 8px; }
  .logo-variant .brand-name { font-size: 21px; }
  .logo-variant .brand-dot { width: 30px; height: 30px; }
  .logo-variant.orange { left: 686px; }
  .logo-variant.orange .brand-dot { background: var(--orange); }
  .logo-variant.sky { left: 842px; }
  .logo-variant.sky .brand-dot { background: var(--sky); }

  .palette { position: absolute; left: 1040px; top: 70px; }
</style>
</head>
<body>

<section class="sheet letterhead" aria-label="Letterhead">
  <div class="rule" style="top:12px"></div>
  <div class="contact-row" style="top:18px">
    <span class="phone">61.400.555017</span>
    <span class="street">48 harbour lane</span>
    <span class="town">north shore sa 5031</span>
    <span class="country">australia</span>
    <span class="email">hello@tallcropnear.com</span>
  </div>

  <p class="salutation">client,</p>

  <div class="letter-body">
    <p>Lorem ipsum dolor sit amet, consectetur adipiscing elit. Donec ut bibendum ligula. Quisque lacinia sagittis porttitor. Integer volutpat blandit mauris eget pulvinar. Aenean ornare, dolor sed venenatis consequat, nisl elit iaculis elit, eget accumsan nunc arcu id justo. Maecenas dui nunc, imperdiet a blandit pretium, adipiscing a lorem. Maecenas eu sagittis ligula. Etiam tincidunt pellentesque turpis quis feugiat. Integer pretium, tellus nec feugiat vulputate, erat velit pulvinar elit, non vulputate quam odio et ipsum. Pellentesque lacinia ante in dui aliquam ut dignissim nulla sollicitudin. Aenean consectetur, magna ut pulvinar consequat, erat est tincidunt quam, sit amet malesuada diam odio quis metus. Aliquam neque justo, adipiscing a consequat ac, ornare sit amet erat. Sed placerat dolor non neque euismod eu egestas eros dapibus. Aenean id fringilla enim. Vivamus non fermentum sem. Pellentesque habitant morbi tristique senectus et netus et malesuada fames ac turpis egestas.</p>
    <p>Sed sit amet odio sem, et lobortis mauris. Fusce ut risus vel turpis imperdiet feugiat. Ut vel justo eget metus fermentum sagittis. Lorem ipsum dolor sit amet, consectetur adipiscing elit. Vivamus elementum molestie ante sed congue. Vivamus condimentum, diam quis tristique iaculis, eros neque fringilla tortor, sed pulvinar ipsum metus id nunc. Donec pellentesque arcu non est commodo consequat. Cras porta leo ut nibh venenatis ultricies. Quisque arcu magna, ornare vitae sollicitudin ac, suscipit eu dolor. Maecenas libero risus, bibendum mattis gravida hendrerit, vehicula sed urna. Vivamus ornare massa quis tellus porta cursus. Etiam posuere rutrum massa id varius. Suspendisse potenti. Duis congue pharetra ligula eu volutpat. Vestibulum eget imperdiet nibh. Curabitur vitae dui nec sem vulputate faucibus nec placerat nunc.</p>
    <p>Integer dictum semper tristique. Cras id lacinia metus. Etiam id augue nisi. Suspendisse potenti. Quisque sed ipsum et risus molestie aliquet. Fusce eu mauris sit amet quam laoreet pulvinar quis sit amet leo. Donec mollis sapien in massa bibendum porta. Nunc blandit molestie libero, ut consequat elit eleifend eu. In rutrum est dolor. Quisque vulputate metus enim, eu venenatis purus. Fusce pellentesque luctus feugiat. Suspendisse potenti. Etiam sed nunc ut dolor eleifend consectetur. Duis enim tellus, porttitor in tristique at, malesuada sit amet metus.</p>
    <p>Vivamus scelerisque ultrices euismod. Proin quis orci sed odio dictum hendrerit eu in ipsum. Maecenas scelerisque tortor metus, non fringilla sapien. Morbi posuere viverra pretium.</p>
  </div>

  <p class="sign-off">sincerely,</p>
  <div class="signature-area" role="img" aria-label="Handwritten signature"></div>

  <div class="brand">
    <span class="brand-name">tallcropnear</span>
    <span class="brand-dot"></span>
  </div>
  <div class="rule" style="top:861px"></div>
</section>

<section class="sheet compliments" aria-label="Compliment slip">
  <div class="rule" style="top:10px"></div>
  <div class="contact-row" style="top:16px">
    <span class="phone">61.400.555017</span>
    <span class="street">48 harbour lane</span>
    <span class="town">north shore sa 5031</span>
    <span class="country">australia</span>
    <span class="email">hello@tallcropnear.com</span>
  </div>
  <p class="title">our compliments :</p>
  <div class="brand">
    <span class="brand-name">tallcropnear</span>
    <span class="brand-dot"></span>
  </div>
  <div class="rule" style="top:280px"></div>
</section>

<div class="logo-variant orange" aria-label="Logo, orange version">
  <span class="brand-dot"></span>
  <span class="brand-name">tallcropnear</span>
</div>
<div class="logo-variant sky" aria-label="Logo, blue version">
  <span class="brand-dot"></span>
  <span class="brand-name">tallcropnear</span>
</div>

<svg class="palette" width="82" height="28" viewBox="0 0 82 28" aria-label="Colour palette">
  <path d="M8 0 C11 8 16 13 16 19 A8 8 0 0 1 0 19 C0 13 5 8 8 0Z" fill="var(--sky)"/>
  <path d="M30 0 C33 8 38 13 38 19 A8 8 0 0 1 22 19 C22 13 27 8 30 0Z" fill="var(--aqua-pale)"/>
  <path d="M52 0 C55 8 60 13 60 19 A8 8 0 0 1 44 19 C44 13 49 8 52 0Z" fill="var(--orange)"/>
  <path d="M74 0 C77 8 82 13 82 19 A8 8 0 0 1 66 19 C66 13 71 8 74 0Z" fill="var(--orange-deep)"/>
</svg>

</body>
</html>
```